Telmoro Business Card

I already have the conplay logo. I need to develop a professional business card layout

Target Market(s)

Business

Industry/Entity Type

Business

Contact Information for Business Card

Company Name: Telmoro Limited

Font styles to use
Sans Serif

Colors

Designer to choose colors to be used in the design.

Requirements
Must have
• Use current logo
• Need two card size options:
• Small Card: 70mm x 28mm (Landscape)
• Square Card: 65mm x 65mm
Nice to have
• I will need 8-10 files for each name, number and email address (details to follow)

```html
<!DOCTYPE html>
<html lang="en">
<head>
<meta charset="utf-8">
<title>Telmoro Limited – Square Business Card</title>
<link rel="stylesheet" href="https://fonts.googleapis.com/css2?family=Roboto+Condensed:wght@700&family=Arimo:wght@400;700&family=Archivo:wght@700&display=swap">
<style>
  :root {
    --page: #ffffff;
    --card: #deff96;
    --navy: #23237e;
    --name: #3b3f8f;
    --orange: #f39200;
    --logo: #8dc21f;
    --band-top: #6cbf3a;
    --band-mid: #29abe2;
    --band-bottom: #0b6db5;
  }
  * { margin: 0; padding: 0; box-sizing: border-box; }
  html, body {
    width: 1200px; height: 938px; overflow: hidden;
    background: var(--page);
  }
  .card {
    position: absolute; left: 245px; top: 106px;
    width: 663px; height: 664px;
    border-radius: 50px;
    background: var(--card);
    overflow: hidden;
  }
  .brand-name {
    position: absolute; left: 64px; top: 41px;
    font-family: "Roboto Condensed", sans-serif;
    font-weight: 700; font-size: 108px; line-height: 1;
    letter-spacing: 17px;
    color: var(--logo);
    white-space: nowrap;
  }
  .company {
    position: absolute; left: 66px; top: 141px;
    font-family: "Roboto Condensed", sans-serif;
    font-weight: 700; font-size: 46px; line-height: 1;
    letter-spacing: -1.5px;
    color: var(--navy);
    white-space: nowrap;
  }
  .person {
    position: absolute; left: 0; right: 0; top: 250px;
    text-align: center; padding-left: 18px;
  }
  .person-name {
    font-family: "Archivo", sans-serif; font-weight: 700;
    font-size: 32px; letter-spacing: 1px; line-height: 1.1;
    color: var(--name);
  }
  .person-role {
    font-family: "Arimo", sans-serif; font-size: 19px;
    color: var(--orange); margin-top: 2px;
  }
  .contacts {
    position: absolute; left: 0; right: 0; top: 332px;
    text-align: center; padding-left: 18px;
    font-family: "Arimo", sans-serif; color: var(--navy);
  }
  .contact { display: flex; flex-direction: column; align-items: center; }
  .contact svg { display: block; }
  .contact-text { font-size: 18px; line-height: 1.2; }
  .contact-phone .contact-text { margin-top: 4px; letter-spacing: 0.5px; }
  .contact-email { margin-top: 8px; }
  .contact-address { margin-top: 8px; }
  .contact-address .contact-text { font-size: 20px; line-height: 1.2; margin-top: 2px; }
  .color-band {
    position: absolute; left: 0; bottom: 0;
    width: 100%; height: 112px;
    background: linear-gradient(180deg, var(--band-top) 0%, var(--band-mid) 45%, var(--band-bottom) 100%);
  }
</style>
</head>
<body>
  <div class="card">
    <div class="brand-name">TELMORO</div>
    <div class="company">TELMORO LIMITED</div>

    <div class="person">
      <div class="person-name">ARJUN MEHTA</div>
      <div class="person-role">Fashion Designer</div>
    </div>

    <div class="contacts">
      <div class="contact contact-phone">
        <svg width="26" height="32" viewBox="0 0 26 32" aria-hidden="true">
          <rect x="4" y="8" width="13" height="22" rx="2" fill="none" stroke="var(--navy)" stroke-width="2"/>
          <line x1="14" y1="8" x2="14" y2="2" stroke="var(--navy)" stroke-width="2"/>
          <rect x="7" y="11" width="7" height="5" fill="var(--navy)"/>
          <g fill="var(--navy)">
            <rect x="7" y="19" width="2" height="2"/><rect x="10" y="19" width="2" height="2"/><rect x="13" y="19" width="2" height="2"/>
            <rect x="7" y="23" width="2" height="2"/><rect x="10" y="23" width="2" height="2"/><rect x="13" y="23" width="2" height="2"/>
          </g>
          <path d="M17 4 Q20 1 23 4" fill="none" stroke="var(--navy)" stroke-width="1"/>
          <path d="M16 2 Q20 -2 25 2" fill="none" stroke="var(--navy)" stroke-width="1"/>
        </svg>
        <div class="contact-text">xx - xxx - xxxxxxx</div>
      </div>

      <div class="contact contact-email">
        <svg width="30" height="18" viewBox="0 0 30 18" aria-hidden="true">
          <rect x="1" y="1" width="20" height="14" fill="none" stroke="var(--navy)" stroke-width="1.6"/>
          <path d="M1 1 L11 9 L21 1" fill="none" stroke="var(--navy)" stroke-width="1.6"/>
          <circle cx="23" cy="12" r="5.5" fill="var(--card)" stroke="var(--navy)" stroke-width="1.6"/>
          <circle cx="23" cy="12" r="2" fill="none" stroke="var(--navy)" stroke-width="1.4"/>
        </svg>
        <div class="contact-text">email@email.com</div>
      </div>

      <div class="contact contact-address">
        <svg width="26" height="22" viewBox="0 0 26 22" aria-hidden="true">
          <path d="M13 1 L1 11 L4 11 L4 21 L10 21 L10 15 L16 15 L16 21 L22 21 L22 11 L25 11 Z" fill="var(--navy)"/>
          <rect x="18" y="2" width="3" height="6" fill="var(--navy)"/>
        </svg>
        <div class="contact-text">Address Street 210 Big City<br>Island - Indonesia</div>
      </div>
    </div>

    <div class="color-band" role="img" aria-label="Decorative multicolour wave pattern along the bottom of the card"></div>
  </div>
</body>
</html>
```